Business card for Property Management consultant

I need a business card for my business LX Vantage - I consult to real estate agents to improve the performance of their Property Management departments (rental houses management). The card needs to be very professional looking, incorporating our logo and my photo plus the line "Develop your Rent Roll to Perform"

Target Market(s)

Real Estate business owners

Industry/Entity Type

Business Consultant

Contact Information for Business Card

Business name - LX Vantage (logo uploaded)
My Name : Marcia Kellaway -
Title : Property Management Consultant

Develop your Rent Roll to perform

Phone : +61 438592716
email : marcia@lxvantage.com.au
website ; www.lxvantage.com.au

Requirements
Must have
• Logo
• My photo
• Very corporate / professional look

```html
<!DOCTYPE html>
<html lang="en">
<head>
<meta charset="utf-8">
<title>LX Vantage – Business Card</title>
<link href="https://fonts.googleapis.com/css2?family=Open+Sans:ital,wght@0,400;0,600;0,700;1,400&display=swap" rel="stylesheet">
<style>
  :root {
    --navy: #4a4fa8;
    --sky: #4aa3df;
    --ice: #dde9f7;
    --lilac: #dcdcef;
    --ink: #1b1c2e;
    --text: #2a2a35;
    --paper: #ffffff;
    --backdrop: #e9eaee;
    --photo-a: #c98a6e;
    --photo-b: #7a3b2a;
  }
  * { box-sizing: border-box; margin: 0; padding: 0; }
  html, body { width: 1200px; height: 873px; overflow: hidden; }
  body {
    background: var(--backdrop);
    font-family: "Open Sans", sans-serif;
    display: flex;
    align-items: center;
    justify-content: center;
    gap: 40px;
  }
  .card {
    position: relative;
    width: 540px;
    height: 310px;
    background: var(--paper);
    overflow: hidden;
    box-shadow: 0 6px 18px rgba(0,0,0,0.12);
  }
  .card-shapes { position: absolute; inset: 0; }

  /* Front */
  .front-brand {
    position: absolute;
    left: 0; right: 0; top: 104px;
    display: flex; align-items: center; justify-content: center; gap: 14px;
  }
  .brand-mark { width: 30px; height: 30px; background: var(--navy); }
  .brand-name {
    font-weight: 700; font-size: 44px; color: var(--ink); letter-spacing: 0.5px;
  }
  .front-tagline {
    position: absolute; left: 0; right: 0; top: 184px;
    text-align: center; font-size: 19px; color: var(--text);
  }

  /* Back */
  .back-brand {
    position: absolute; left: 150px; top: 40px;
    display: flex; align-items: center; gap: 9px;
  }
  .back-brand .brand-mark { width: 18px; height: 18px; }
  .back-brand .brand-name { font-size: 26px; }
  .contact-list {
    position: absolute; left: 60px; top: 150px; width: 214px;
    list-style: none;
  }
  .contact-item {
    display: flex; align-items: center; justify-content: flex-end; gap: 9px;
    height: 30px; font-size: 12.5px; color: var(--text);
  }
  .contact-icon {
    width: 22px; height: 22px; background: var(--navy);
    display: flex; align-items: center; justify-content: center; flex: none;
  }
  .person {
    position: absolute; right: 16px; top: 66px; text-align: right; color: var(--paper);
  }
  .person-name { font-weight: 700; font-size: 19px; }
  .person-title { font-style: italic; font-size: 11px; margin-top: 2px; }
  .portrait {
    position: absolute; left: 405px; top: 148px;
    width: 96px; height: 96px; border-radius: 50%;
    border: 4px solid var(--paper);
    background: radial-gradient(circle at 50% 40%, var(--photo-a), var(--photo-b));
  }
</style>
</head>
<body>

  <section class="card card-front">
    <svg class="card-shapes" width="540" height="310" viewBox="0 0 540 310">
      <polygon points="0,0 540,0 540,16 0,6" fill="var(--sky)"/>
      <polygon points="0,310 540,310 540,298 0,284" fill="var(--navy)"/>
    </svg>
    <div class="front-brand">
      <span class="brand-mark"></span>
      <span class="brand-name">LX Vantage</span>
    </div>
    <p class="front-tagline">Develop your Rent Roll to Perform</p>
  </section>

  <section class="card card-back">
    <svg class="card-shapes" width="540" height="310" viewBox="0 0 540 310">
      <polygon points="70,0 150,0 120,120" fill="var(--ice)"/>
      <polygon points="0,70 50,60 115,115 0,175" fill="var(--lilac)"/>
      <polygon points="380,0 398,0 258,310 240,310" fill="var(--sky)"/>
      <polygon points="398,0 540,0 540,310 258,310" fill="var(--navy)"/>
    </svg>

    <div class="back-brand">
      <span class="brand-mark"></span>
      <span class="brand-name">LX Vantage</span>
    </div>

    <ul class="contact-list">
      <li class="contact-item">+61 438592716
        <span class="contact-icon">
          <svg width="12" height="14" viewBox="0 0 12 14"><rect x="2" y="0.8" width="8" height="12.4" rx="1.4" fill="none" stroke="#fff" stroke-width="1.4"/><line x1="5" y1="10.6" x2="7" y2="10.6" stroke="#fff" stroke-width="1.4"/></svg>
        </span>
      </li>
      <li class="contact-item">marcia@lxvantage.com.au
        <span class="contact-icon">
          <svg width="14" height="10" viewBox="0 0 14 10"><rect x="0.7" y="0.7" width="12.6" height="8.6" fill="none" stroke="#fff" stroke-width="1.3"/><polyline points="0.7,0.7 7,5.5 13.3,0.7" fill="none" stroke="#fff" stroke-width="1.3"/></svg>
        </span>
      </li>
      <li class="contact-item">www.lxvantage.com.au
        <span class="contact-icon">
          <svg width="14" height="14" viewBox="0 0 14 14"><circle cx="7" cy="7" r="6" fill="none" stroke="#fff" stroke-width="1.3"/><ellipse cx="7" cy="7" rx="2.6" ry="6" fill="none" stroke="#fff" stroke-width="1.1"/><line x1="1" y1="7" x2="13" y2="7" stroke="#fff" stroke-width="1.1"/></svg>
        </span>
      </li>
    </ul>

    <div class="person">
      <p class="person-name">Marcia Kellaway</p>
      <p class="person-title">Property Management Consultant</p>
    </div>
    <div class="portrait" role="img" aria-label="Portrait photo of Marcia Kellaway"></div>
  </section>

</body>
</html>
```